CPA Firm Stationary & Business Cards
Whitfield & Partners CPAs PSC
CPA Firm Stationary & Business Cards - Financial Services
Creative Brief
Professional
Martin L. Dowse, CPA
Shareholder
4815 Tillamore Ave. Suite 1 Fairmont Vale, IN 47999
mdowse@wpfcpa.net
www.wpfcpa.net
We are a CPA (Certified Public Accountant) firm, in business since 1924. In addition to Business Cards, I would also like to see designs for Letterheads and Envelopes.
Your choice. At a minimum, it should include the "W" logo.In addition to Business Cards, I would also like to see designs for Letterheads and Envelopes.

```html
<!DOCTYPE html>
<html lang="en">
<head>
<meta charset="utf-8">
<title>Whitfield &amp; Partners CPAs PSC — Business Card</title>
<link rel="stylesheet" href="https://fonts.googleapis.com/css2?family=Montserrat:wght@400;500;600&display=swap">
<style>
  :root {
    --page: #e9ebee;
    --card-white: #ffffff;
    --brand-blue: #1e5fd8;
    --brand-deep: #0b2f8f;
    --brand-light: #3f8df0;
    --ink: #2b3140;
    --ink-soft: #6a7282;
    --rule: #c9d3e6;
    --swoosh-grey: #b8c4d8;
  }
  * { margin: 0; padding: 0; box-sizing: border-box; }
  html, body { width: 1200px; height: 1060px; overflow: hidden; }
  body {
    background: var(--page);
    font-family: "Montserrat", sans-serif;
    color: var(--ink);
    position: relative;
  }
  .card {
    position: absolute;
    left: 250px;
    width: 700px;
    height: 400px;
    border-radius: 22px;
    overflow: hidden;
    box-shadow: 0 10px 30px rgba(20, 30, 60, 0.18);
  }
  .card-front { top: 90px; background: var(--card-white); }
  .card-back {
    top: 570px;
    background: linear-gradient(160deg, var(--brand-light) 0%, var(--brand-blue) 45%, var(--brand-deep) 100%);
    display: flex; align-items: center; justify-content: center;
  }
  .swoosh { position: absolute; inset: 0; width: 100%; height: 100%; }
  .brand {
    position: absolute; left: 48px; top: 56px;
    display: flex; align-items: center; gap: 16px;
  }
  .brand-dot { width: 44px; height: 44px; border-radius: 50%; background: var(--brand-blue); flex: none; }
  .brand-name {
    font-weight: 500; color: var(--brand-blue);
    font-size: 22px; letter-spacing: 2px; line-height: 1.25;
    text-transform: uppercase;
  }
  .person { position: absolute; left: 48px; top: 200px; }
  .person-name { font-size: 20px; font-weight: 600; color: var(--brand-blue); }
  .person-title { font-size: 14px; color: var(--ink-soft); margin-top: 6px; }
  .divider {
    position: absolute; left: 400px; top: 160px; width: 1px; height: 160px;
    background: var(--rule);
  }
  .contact { position: absolute; left: 424px; top: 160px; list-style: none; font-size: 12.5px; }
  .contact li { display: flex; align-items: center; gap: 10px; height: 27px; white-space: nowrap; }
  .contact svg { width: 14px; height: 14px; fill: var(--brand-blue); flex: none; }
  .back-name {
    color: #fff; font-weight: 500; text-transform: uppercase;
    font-size: 34px; letter-spacing: 4px; text-align: center; line-height: 1.3;
  }
</style>
</head>
<body>
  <section class="card card-front">
    <svg class="swoosh" viewBox="0 0 700 400" preserveAspectRatio="none" aria-hidden="true">
      <path d="M700 280 C600 345 520 372 410 400 L430 400 C520 385 600 360 700 300 Z" fill="#b8c4d8"/>
      <path d="M700 300 C600 360 520 385 430 400 L700 400 Z" fill="#1e5fd8"/>
    </svg>
    <div class="brand">
      <span class="brand-dot"></span>
      <div class="brand-name">Whitfield<br>&amp; Partners CPAs PSC</div>
    </div>
    <div class="person">
      <div class="person-name">Martin L. Dowse, CPA</div>
      <div class="person-title">Shareholder</div>
    </div>
    <div class="divider"></div>
    <ul class="contact">
      <li><svg viewBox="0 0 24 24"><path d="M12 2a7 7 0 0 0-7 7c0 5 7 13 7 13s7-8 7-13a7 7 0 0 0-7-7zm0 9.5A2.5 2.5 0 1 1 12 6.5a2.5 2.5 0 0 1 0 5z"/></svg>4815 Tillamore Ave. Suite 1</li>
      <li><svg viewBox="0 0 24 24"><circle cx="12" cy="12" r="3"/></svg>Fairmont Vale, IN 47999</li>
      <li><svg viewBox="0 0 24 24"><path d="M6.6 10.8a15 15 0 0 0 6.6 6.6l2.2-2.2c.3-.3.7-.4 1-.2 1.1.4 2.3.6 3.6.6.6 0 1 .4 1 1V20c0 .6-.4 1-1 1A17 17 0 0 1 3 4c0-.6.4-1 1-1h3.5c.6 0 1 .4 1 1 0 1.3.2 2.5.6 3.6.1.3 0 .7-.2 1z"/></svg>P 555.201.0142</li>
      <li><svg viewBox="0 0 24 24"><rect x="4" y="8" width="16" height="10" rx="2"/><rect x="7" y="3" width="10" height="5"/></svg>F 555.201.0143</li>
      <li><svg viewBox="0 0 24 24"><path d="M3 5h18v14H3zm2 2v.5l7 5 7-5V7z"/></svg>mdowse@wpfcpa.net</li>
      <li><svg viewBox="0 0 24 24"><path d="M12 2a10 10 0 1 0 0 20 10 10 0 0 0 0-20zm0 2c1 1.3 1.8 3.5 2 6h-4c.2-2.5 1-4.7 2-6zm-2 8h4c-.2 2.5-1 4.7-2 6-1-1.3-1.8-3.5-2-6z"/></svg>www.wpfcpa.net</li>
    </ul>
  </section>

  <section class="card card-back">
    <div class="back-name">Whitfield<br>&amp; Partners CPAs PSC</div>
  </section>
</body>
</html>
```